Crestline Venture Partners Business Card Redesign Project

CRESTLINE VENTURE PARTNERS
Our company needs to have its business cards redesigned as the current design no longer reflects the business brand or attracts the type of clientele we are seeking.

MUST LOOK
★ Upmarket
★ Reflect Quality
★ Corporate feel
★ Professional
★ Innovative
★ Colourful

MUST PROMOTE
★ Market Leader
★ Knowledge
★ Expertise
★ Experience
★ Solutions
★ Advice

MUST FEEL
★ Classy
★ Elegant
★ Savvy
★ Edgy
★ Upbeat

WHAT WE DO
Crestline Venture Partners provides project management and project controls consultancy services to companies in many industry sectors, within Australia and overseas. My company has developed a business brand through forging strong business relationships within industry. We provide innovative tools, concepts and solutions to management teams to assist them in better plan and managing there project portfolios.

SECTORS OF INDUSTRY WE SERVICE
★Oil & Gas
★Minerals & Metals
★Petrochemical
★Manufacturing
★Building & Construction
★Telecommunications
★Rail
★Civil

BUSINESS CARD DETAILS REQUIRED ON FRONT
Marcus Delane
Business Owner
Tel: 0438519627
Email: marcusdelane@crestlineventurepartners.com
Website: www.crestlineventurepartners.com.au

BUSINESS CARD DETAILS REQUIRED ON BACK
INSIGHT | STRATEGY | DELIVERY | RESULTS

ATTACHMENTS

Target Market(s)

Oil & Gas I Mining & Resources I Industry in General
Upmarket Clientele
Corporate World

Industry/Entity Type

Industry

Requirements
Must have
• Must be creative and a unique design
The business card must have information on the front and back

```html
<!DOCTYPE html>
<html lang="en">
<head>
<meta charset="utf-8">
<title>Crestline Venture Partners – Business Card</title>
<link rel="stylesheet" href="https://fonts.googleapis.com/css2?family=Montserrat:wght@400;500;700;800&display=swap">
<style>
  :root {
    --backdrop: #2b2b2d;
    --card: #f4f4f4;
    --card-edge: #e2e2e2;
    --ink: #1a1a1c;
    --ink-soft: #3a3a3c;
    --accent: #e0121d;
  }
  * { box-sizing: border-box; margin: 0; padding: 0; }
  html, body { width: 1200px; height: 900px; overflow: hidden; }
  body {
    background: var(--backdrop);
    font-family: "Montserrat", Arial, sans-serif;
    position: relative;
  }
  .card {
    position: absolute;
    left: 250px;
    width: 700px;
    height: 400px;
    border-radius: 28px;
    background: linear-gradient(135deg, #ffffff 0%, var(--card) 55%, var(--card-edge) 100%);
    overflow: hidden;
  }
  .card--back { top: 35px; }
  .card--front { top: 465px; }

  .brand { position: absolute; display: flex; align-items: center; gap: 14px; }
  .brand__mark { width: 34px; height: 34px; background: var(--accent); flex: none; }
  .brand__name {
    font-weight: 800;
    font-size: 27px;
    color: var(--ink);
    letter-spacing: -0.3px;
    white-space: nowrap;
  }
  .tagline {
    position: absolute;
    font-weight: 700;
    font-size: 12.5px;
    color: var(--ink-soft);
    white-space: nowrap;
  }

  /* back */
  .card--back .brand { left: 80px; top: 150px; }
  .card--back .tagline { left: 128px; top: 196px; }
  .values {
    position: absolute;
    right: 46px;
    bottom: 40px;
    font-size: 13px;
    font-weight: 500;
    letter-spacing: 1.5px;
    color: var(--ink-soft);
    white-space: nowrap;
  }

  /* front */
  .card--front .brand { left: 44px; top: 62px; }
  .card--front .tagline { left: 92px; top: 106px; }
  .contact { position: absolute; left: 248px; top: 160px; }
  .contact__name { font-size: 28px; font-weight: 500; color: var(--accent); line-height: 1.1; }
  .contact__role { font-size: 17px; font-weight: 500; color: var(--ink); margin-top: 4px; }
  .contact__list { list-style: none; margin-top: 24px; }
  .contact__item {
    display: flex; align-items: center; gap: 10px;
    font-size: 15.5px; color: var(--ink); height: 30px; white-space: nowrap;
  }
  .contact__icon { width: 20px; height: 20px; flex: none; }
  .social { position: absolute; left: 44px; bottom: 40px; display: flex; gap: 8px; }
  .social__tile { width: 24px; height: 24px; background: var(--accent); border-radius: 2px; }
</style>
</head>
<body>

<section class="card card--back" aria-label="Card back">
  <div class="brand">
    <span class="brand__mark"></span>
    <span class="brand__name">CRESTLINE VENTURE PARTNERS</span>
  </div>
  <p class="tagline">Delivering Clear Venture Planning and Portfolio Advisory Services</p>
  <p class="values">INSIGHT | STRATEGY | DELIVERY | RESULTS</p>
</section>

<section class="card card--front" aria-label="Card front">
  <div class="brand">
    <span class="brand__mark"></span>
    <span class="brand__name">CRESTLINE VENTURE PARTNERS</span>
  </div>
  <p class="tagline">Delivering Clear Venture Planning and Portfolio Advisory Services</p>

  <div class="contact">
    <p class="contact__name">Marcus Delane</p>
    <p class="contact__role">Business Owner</p>
    <ul class="contact__list">
      <li class="contact__item">
        <svg class="contact__icon" viewBox="0 0 20 20" aria-hidden="true">
          <circle cx="10" cy="10" r="10" fill="var(--accent)"/>
          <path d="M6 7.5c0-1 .8-1.5 1.5-1.5h5c.7 0 1.5.5 1.5 1.5v1h-2v-1h-4v1H6z M6.5 9.5h7l1 4h-9z" fill="#fff"/>
        </svg>
        0438 519 627
      </li>
      <li class="contact__item">
        <svg class="contact__icon" viewBox="0 0 20 20" aria-hidden="true">
          <circle cx="10" cy="10" r="10" fill="var(--accent)"/>
          <rect x="5" y="6.5" width="10" height="7" fill="#fff"/>
          <path d="M5 6.5l5 4 5-4" fill="none" stroke="var(--accent)" stroke-width="1"/>
        </svg>
        marcusdelane@crestlineventurepartners.com
      </li>
      <li class="contact__item">
        <svg class="contact__icon" viewBox="0 0 20 20" aria-hidden="true">
          <circle cx="10" cy="10" r="10" fill="var(--accent)"/>
          <g fill="none" stroke="#fff" stroke-width="1.1">
            <circle cx="10" cy="10" r="5.5"/>
            <ellipse cx="10" cy="10" rx="2.4" ry="5.5"/>
            <path d="M4.5 10h11M5.5 7h9M5.5 13h9"/>
          </g>
        </svg>
        www.crestlineventurepartners.com.au
      </li>
    </ul>
  </div>

  <div class="social" aria-label="Social links">
    <span class="social__tile"></span>
    <span class="social__tile"></span>
    <span class="social__tile"></span>
  </div>
</section>

</body>
</html>
```